Harbor Sushi & Steak Dinner Menu

I'm looking for a MENU design with a particular feel. I want to have a base template made that I can then use for future alterations to the menu; ie I can go in and change out different entrees as the menu changes but the template will remain the same. (Ideally it would be in an Apple Pages format.). Also ideally - dinner menu will occupy 2 pages 8.5 x 11. The restaurant's name is Harbor. It is a MODERN steak house that will also feature Sushi, a Raw Bar, Exquisite Cocktails and a sophisticated nightlife crowd. I have attached our LOGO, a secondary logo that we will be featuring throughout the project including on the menu cover (the gold U). Finally - I have attached the content that we would like to see. AGAIN - I REITERATE: High end dining and lounge atmosphere. A couple of restaurants / menus that I love are Morvendel in NYC and Pellucid Steakhouse in Long Island NY. Please do not duplicate - just trying to offer some suggestions.

Requirements
Must have
• A sophisticated and elegant feel without being stuffy or old.

```html
<!DOCTYPE html>
<html lang="en">
<head>
<meta charset="utf-8">
<title>Harbor Sushi &amp; Steak — Dinner Menu</title>
<link rel="stylesheet" href="https://fonts.googleapis.com/css2?family=Outfit:wght@400;600&family=Poppins:wght@600;700&display=swap">
<style>
  :root {
    --slate: #3a4251;
    --gold: #f1c21b;
    --ink: #ffffff;
    --sketch: rgba(150, 152, 165, 0.28);
    --ribbon-top: #c8c296;
    --ribbon-bottom: #b06a4c;
  }
  html, body { margin: 0; padding: 0; overflow: hidden; }
  body { width: 927px; height: 1200px; }
  .menu-page {
    position: relative;
    width: 927px;
    height: 1200px;
    background: var(--slate);
    color: var(--ink);
    font-family: "Outfit", sans-serif;
    overflow: hidden;
  }
  .brand {
    position: absolute;
    left: 52px; top: 76px;
    width: 290px;
    display: flex; align-items: center; gap: 14px;
  }
  .brand-dot {
    width: 22px; height: 22px; border-radius: 50%;
    background: var(--gold);
  }
  .brand-name {
    margin: 0;
    font-family: "Poppins", sans-serif;
    font-size: 50px; font-weight: 600; letter-spacing: 8px;
    color: var(--gold);
    line-height: 1;
  }
  .ribbon { position: absolute; left: 771px; top: 0; }
  .sketch {
    position: absolute;
    background: var(--sketch);
    border-radius: 40px;
  }
  .sketch-pizza { left: 532px; top: 68px; width: 176px; height: 186px; border-radius: 30px 60px 40px 40px; }
  .sketch-burger { left: 330px; top: 238px; width: 210px; height: 176px; border-radius: 50%; }
  .sketch-corndog { left: 676px; top: 484px; width: 180px; height: 128px; border-radius: 60px; }
  .sketch-cup { left: 388px; top: 946px; width: 128px; height: 228px; border-radius: 20px 20px 30px 30px; }

  .section { position: absolute; }
  .section h2 {
    margin: 0 0 14px;
    font-family: "Poppins", sans-serif;
    font-size: 24px; font-weight: 700;
    color: var(--gold);
    line-height: 30px;
  }
  .section ul { list-style: none; margin: 0; padding: 0; }
  .section li, .section p {
    font-size: 16px; line-height: 20px; margin: 0;
    white-space: nowrap;
  }
  .section p + p { margin-top: 9px; }
  .section strong { font-weight: 600; }
  .sides li { line-height: 20.8px; }
  .section .raw-plate { margin-top: 10px; }

  .sushi-sashimi { left: 57px; top: 258px; }
  .sushi-platters { left: 628px; top: 296px; }
  .classic-rolls { left: 56px; top: 497px; }
  .special-rolls { left: 56px; top: 699px; }
  .sides { left: 623px; top: 575px; }
  .raw-bar { left: 56px; top: 921px; }
  .raw-bar h2 { margin-bottom: 20px; }
  .seafood-platters { left: 530px; top: 921px; }
  .seafood-platters h2 { margin-bottom: 18px; }
  .seafood-platters p { padding-left: 4px; }
  .section.seafood-platters p + p { margin-top: 0; }
</style>
</head>
<body>
<main class="menu-page">
  <header class="brand">
    <span class="brand-dot"></span>
    <h1 class="brand-name">HARBOR</h1>
  </header>

  <svg class="ribbon" width="76" height="131" viewBox="0 0 76 131" aria-hidden="true">
    <defs>
      <linearGradient id="ribbonFill" x1="0" y1="0" x2="0" y2="1">
        <stop offset="0" stop-color="#c8c296"/>
        <stop offset="1" stop-color="#b06a4c"/>
      </linearGradient>
    </defs>
    <path d="M0 0H76V131L38 120L0 131Z" fill="url(#ribbonFill)"/>
  </svg>

  <div class="sketch sketch-pizza" role="img" aria-label="Line sketch of a pizza slice"></div>
  <div class="sketch sketch-burger" role="img" aria-label="Line sketch of a burger"></div>
  <div class="sketch sketch-corndog" role="img" aria-label="Line sketch of a corn dog"></div>
  <div class="sketch sketch-cup" role="img" aria-label="Line sketch of a drink cup with straw"></div>

  <section class="section sushi-sashimi">
    <h2>SUSHI / SASHIMI</h2>
    <ul>
      <li>Toro; blue fin tuna belly (gf)</li>
      <li>Unagi; fresh water eel (gf)</li>
      <li>Ebi; cooked shrimp (gf)</li>
      <li>Sake; salmon (gf)</li>
      <li>Hamachi; yellowtail (gf)</li>
      <li>Madai; red snapper (gf)</li>
      <li>Uni; sea urchin (gf)</li>
      <li>Maguro; tuna (gf)</li>
      <li>Hirame; fluke (gf)</li>
    </ul>
  </section>

  <section class="section sushi-platters">
    <h2>SUSHI PLATTERS</h2>
    <p><strong>Small :</strong>&nbsp; Five Pieces assorted sushi,<br>nine pieces sashimi, spicy tuna roll (gf)</p>
    <p><strong>Large :</strong>&nbsp; Eight Pieces assorted<br>sushi, eighteen pieces of sashimi,<br>alaskan roll, rainbow roll (gf)</p>
  </section>

  <section class="section classic-rolls">
    <h2>CLASSIC ROLLS</h2>
    <ul>
      <li>Yellowtail; inside out roll with scallions (gf)</li>
      <li>Spicy Tuna or Salmon or Yellowtail; spicy mayo</li>
      <li>California: crab meat, cucumber and avocado (gf)</li>
      <li>Vegetable: avocado, cucumber, asparagus and pickled reddish (gf)</li>
      <li>Spider: soft shell crab and avocado with eel sauce</li>
      <li>Shrimp Tempura: deep fried tempura shrimp and eel sauce</li>
      <li>Alaskan; salmon and avocado (gf)</li>
    </ul>
  </section>

  <section class="section special-rolls">
    <h2>SPECIAL ROLLS</h2>
    <ul>
      <li>The Harbor:&nbsp; tuna, salmon, yellowtail, avocado, spicy mayo, soy bean paper</li>
      <li>King Crab Rainbow:&nbsp; king crab, avocado, cucumbers, assorted fish on top</li>
      <li>Empress:&nbsp; Shrimp tempura, spicy tuna on top, eel sauce, spicy mayo</li>
      <li>Spicy Girl:&nbsp; Spicy crunchy crab meat, cucumber, shrimp on top</li>
      <li>Dragon:&nbsp; Eel, cucumber, avocado, and tobiko on top, eel sauce</li>
      <li>Yummy:&nbsp; spicy crunchy salmon, avocado, mango and salmon on top</li>
      <li>No. 9:&nbsp; Shrimp Tempura, avocado, kani, spicy mayo, tobiko</li>
      <li>Sunrise Roll:&nbsp; spicy crunchy tuna and avocado, spicy crunchy salmon on top</li>
    </ul>
  </section>

  <section class="section sides">
    <h2>SIDES</h2>
    <ul>
      <li>Mashed Idaho Potatoes</li>
      <li>Bacon, Sweet Corn, Caramelized</li>
      <li>Vidalia Onion fingerling potatoes</li>
      <li>Roasted Peanut Potatoes</li>
      <li>Creamed Spinach</li>
      <li>Sautéed Spinach</li>
      <li>Grilled Asparagus</li>
      <li>French Beans</li>
      <li>Israeli Cous Cous</li>
      <li>Sweet Potato Steak Fries</li>
      <li>Corn Skillet</li>
    </ul>
  </section>

  <section class="section raw-bar">
    <h2>SEAFOOD RAW BAR</h2>
    <ul>
      <li>Lobster Cocktail</li>
      <li>Shrimp Cocktail</li>
      <li>Clams on the Half Shell</li>
      <li>Oysters on the Half Shell</li>
      <li>Colossal Crab Cocktail</li>
    </ul>
    <p class="raw-plate">Raw Bar Plate for One:<br>Two Shrimp, Half of a One Pound Lobster,<br>Two Clams, One East Coast Oyster,<br>One West Coast Oyster</p>
  </section>

  <section class="section seafood-platters">
    <h2>SEAFOOD PLATTERS (gf)</h2>
    <p>Shrimp, Oysters, Clams, Lobster and Crab</p>
    <p>Large or Colossal</p>
  </section>
</main>
</body>
</html>
```